Upmarket Bathroom and Kitchen ware supplier needs a classy business card design

We are a company based in Fiji, we sell plumbing ware (Kitchen and bathroom taps, Basins,showers, toilets etc) through up market show rooms to individuals and directly through Architects and designers of resorts and holiday houses for new builds and renovations. we are wanting to upgrade our over all look and brand. we are starting with a new logo but will be rebranding the whole business. This project is for a business card design for my management and tales team I would like it to be dark, classy and interesting

Target Market(s)

Resort directors and Management, High end holiday home owners

Contact Information for Business Card

Neil Dawson
Director
+64219473815

Colors

Designer to choose colors to be used in the design.

Requirements
Must have
• Must have an upmarket appearance I like darker charcoal shades but will be guided by the designers
• Please any catch phrases like "Crafting remarkable living rooms" this belongs tpo one of our suppliers so can not be used.
Nice to have
• Double sided, so front dedicated to logo provided and back info about the business and the person.

```html
<!DOCTYPE html>
<html lang="en">
<head>
<meta charset="utf-8">
<title>Lagoon Fixtures – Business Card</title>
<link rel="stylesheet" href="https://fonts.googleapis.com/css2?family=Montserrat:wght@300;400;700&display=swap">
<style>
  :root {
    --backdrop: #d8d5d1;
    --card: #1f1f20;
    --card-edge: #141415;
    --brand-grey: #9c9c9c;
    --ghost: #262627;
    --ink: #f2f2f2;
  }
  * { box-sizing: border-box; margin: 0; padding: 0; }
  html, body {
    width: 1200px;
    height: 800px;
    overflow: hidden;
    background: var(--backdrop);
    font-family: "Montserrat", sans-serif;
  }
  .canvas {
    position: relative;
    width: 1200px;
    height: 800px;
  }
  .card {
    position: absolute;
    top: 257px;
    width: 500px;
    height: 286px;
    background: var(--card);
    box-shadow: 0 6px 0 var(--card-edge), 0 18px 40px rgba(0,0,0,0.25);
    overflow: hidden;
  }
  .card--front { left: 70px; }
  .card--back { left: 630px; }

  .brand {
    position: absolute;
    display: flex;
    align-items: center;
    gap: 12px;
    color: var(--brand-grey);
    font-weight: 300;
  }
  .brand__square {
    width: 14px;
    height: 14px;
    background: var(--brand-grey);
  }
  .brand__name {
    display: flex;
    flex-direction: column;
    line-height: 1.25;
  }
  .brand__main {
    font-size: 22px;
    letter-spacing: 0.42em;
  }
  .brand__sub {
    font-size: 9px;
    letter-spacing: 0.5em;
    align-self: flex-end;
    margin-right: -0.5em;
  }
  .card--front .brand {
    left: 50%;
    top: 50%;
    transform: translate(-50%, -50%);
  }
  .card--back .brand {
    right: 34px;
    top: 40px;
  }

  .ghost-word {
    position: absolute;
    left: 30px;
    bottom: -14px;
    font-size: 96px;
    font-weight: 300;
    letter-spacing: 0.28em;
    color: var(--ghost);
    white-space: nowrap;
  }

  .contact {
    position: absolute;
    left: 34px;
    bottom: 44px;
    color: var(--ink);
  }
  .contact__name {
    font-size: 24px;
    letter-spacing: 0.04em;
    text-transform: uppercase;
    line-height: 1.1;
  }
  .contact__first { font-weight: 300; }
  .contact__last { font-weight: 700; }
  .contact__line {
    margin-top: 6px;
    font-size: 12px;
    font-weight: 700;
    letter-spacing: 0.03em;
    text-transform: uppercase;
  }
</style>
</head>
<body>
<main class="canvas">
  <section class="card card--front" aria-label="Card front">
    <div class="brand">
      <span class="brand__square"></span>
      <span class="brand__name">
        <span class="brand__main">LAGOON</span>
        <span class="brand__sub">FIXTURES</span>
      </span>
    </div>
  </section>

  <section class="card card--back" aria-label="Card back">
    <span class="ghost-word" aria-hidden="true">LAGOON</span>
    <div class="brand">
      <span class="brand__square"></span>
      <span class="brand__name">
        <span class="brand__main">LAGOON</span>
        <span class="brand__sub">FIXTURES</span>
      </span>
    </div>
    <div class="contact">
      <p class="contact__name"><span class="contact__first">Neil</span> <span class="contact__last">Dawson</span></p>
      <p class="contact__line">Director • +64219473815</p>
    </div>
  </section>
</main>
</body>
</html>
```